Press Release A BRAMBLEWOOD AND A CLEVER PELICAN book/website/on-line farmshop

I am ex-stylist.
In a few months time I will be releasing my first coffee table book/website/online farm shop. I need a short, sharp, but really beautifully pulled together and eye-pleasing one page PRESS RELEASE to send out to editors of interior and lifestyle magazines. I need to include the book cover plus publisher, a little about me, a few photographs from the book as a teaser, the new BRAMBLEWOOD logo that is used on jars boxes and cartons when produce is sold, and anything else you think would make for great content within the above-mentioned publications.
I will obviously need to work with you in terms of copy to include on the page as this is quite personal. Maybe start with some of the info from the Bio and we can tweak it from there?
I will also be launching my website at the same time which will link to my own BRAMBLEWOOD brand honey/eggs along with gorgeous produce boxes - available to purchase from The Bramblewood (logo attached). Need someone who can put this PRESS RELEASE together in a concise but authentic-to- my -style kind of way. Needs to look UBER clean, styled, and editorial. Have other pics and info but thought these would be a great place to start and give you an idea of the DNA of me/the book etc.

Target Market(s)

MAGAZINES

Industry/Entity Type

Lifestyle

Font styles to use
Serif

Requirements
Must have
• PRESS RELEASE ON TITLE
A BRAMBLEWOOD AND A CLEVVER PELICAN ON TITLE
Should not have
• "PROOF" ON ANY OF THE PICTURES
CHIRPLINE, FRIENDLINK OR PHONE NUMBER

```html
<!DOCTYPE html>
<html lang="en">
<head>
<meta charset="utf-8">
<title>A Bramblewood and a Clever Pelican – Press Release</title>
<link rel="stylesheet" href="https://fonts.googleapis.com/css2?family=Oswald:wght@300;400;500&family=Tinos&display=swap">
<style>
  :root {
    --yellow: #f5d10a;
    --red: #e1061c;
    --ink: #111111;
    --body: #3a3a3a;
    --white: #ffffff;
    --footer: #121212;
    --hero-dark: #0d0c0b;
  }
  * { margin: 0; padding: 0; box-sizing: border-box; }
  html, body { width: 1200px; height: 3702px; overflow: hidden; }
  body {
    position: relative;
    background: var(--white);
    font-family: "Oswald", sans-serif;
    color: var(--body);
  }

  /* Hero */
  .hero {
    position: absolute; left: 0; top: 0; width: 1200px; height: 929px;
    background:
      linear-gradient(180deg, rgba(0,0,0,.85) 0%, rgba(0,0,0,.35) 18%, rgba(0,0,0,.45) 60%, rgba(0,0,0,.7) 100%),
      radial-gradient(ellipse at 30% 45%, #5a5148 0%, #2a2520 45%, var(--hero-dark) 100%);
  }
  .brand {
    position: absolute; top: 52px; width: 100%; text-align: center;
    font-weight: 500; font-size: 64px; line-height: 84px; color: var(--yellow);
    letter-spacing: -1px;
  }
  .hero-title {
    position: absolute; top: 312px; width: 100%; text-align: center;
    font-weight: 500; font-size: 88px; line-height: 114px; color: var(--white);
    letter-spacing: -1.5px;
  }
  .hero-title .accent { color: var(--yellow); }
  .hero-credit {
    position: absolute; top: 596px; width: 100%; text-align: center;
    font-weight: 500; font-size: 36px; line-height: 56px; color: var(--white);
    letter-spacing: -0.5px;
  }

  /* Intro */
  .intro-card {
    position: absolute; left: 92px; top: 735px; width: 1014px; height: 200px;
    background: var(--white);
  }
  .intro {
    position: absolute; left: 130px; top: 803px; width: 940px;
    font-weight: 300; font-size: 33px; line-height: 65px; text-align: center;
    color: var(--body);
  }
  .intro p + p { margin-top: 64px; }

  /* Book */
  .book-frame {
    position: absolute; left: 92px; top: 1335px; width: 1016px; height: 762px;
    background: var(--white);
    box-shadow: 0 30px 36px rgba(0,0,0,.35), 0 0 8px rgba(0,0,0,.12);
  }
  .book-cover {
    position: absolute; left: 30px; top: 33px; width: 956px; height: 696px;
    display: flex; background: #0e0e0e;
  }
  .cover-back {
    width: 461px; height: 100%; padding: 124px 30px 0;
    background: linear-gradient(180deg, #2a2a2a 0%, #3b3b3b 40%, #1b1b1b 100%);
    font-family: "Tinos", serif; font-size: 17px; line-height: 22px;
    color: #e6e6e6; text-align: center;
  }
  .cover-back p + p { margin-top: 22px; }
  .cover-spine {
    width: 57px; height: 100%; background: #151515;
    display: flex; align-items: center; justify-content: center;
  }
  .spine-text {
    writing-mode: vertical-rl; white-space: nowrap;
    font-weight: 500; font-size: 16px; color: var(--white); letter-spacing: .5px;
  }
  .spine-text .spine-gap { display: inline-block; height: 60px; }
  .cover-front {
    position: relative; width: 438px; height: 100%; overflow: hidden;
  }
  .cover-photo {
    position: absolute; inset: 0;
    background:
      radial-gradient(ellipse at 50% 55%, #d9dcd8 0%, #8e918c 16%, #3a3d3f 40%, #14181b 72%),
      #14181b;
  }
  .cover-title {
    position: absolute; top: 10px; width: 100%; text-align: center;
    font-weight: 300; font-size: 52px; line-height: 62px; color: var(--white);
    letter-spacing: -1.5px; white-space: nowrap;
  }
  .cover-title .accent { color: var(--yellow); }
  .cover-credit {
    position: absolute; top: 150px; width: 100%; text-align: center;
    font-size: 11px; line-height: 14px; color: #dddddd; letter-spacing: .5px;
    white-space: nowrap;
  }
  .cover-author {
    position: absolute; bottom: 22px; width: 100%; text-align: center;
    font-weight: 500; font-size: 34px; color: var(--white);
  }

  /* Author */
  .portrait-ring {
    position: absolute; left: 323px; top: 2193px; width: 554px; height: 554px;
    border-radius: 50%; border: 17px solid var(--yellow); background: var(--white);
  }
  .portrait {
    position: absolute; left: 41px; top: 41px; width: 438px; height: 438px;
    border-radius: 50%;
    background: linear-gradient(180deg, #9a9a95 0%, #6d6a63 45%, #2f4a7a 75%, #25407a 100%);
  }
  .about-title {
    position: absolute; top: 2806px; width: 100%; text-align: center;
    font-weight: 500; font-size: 68px; line-height: 86px; color: var(--ink);
    letter-spacing: -1px;
  }
  .about-title .accent { color: var(--red); }
  .about-text {
    position: absolute; left: 130px; top: 2948px; width: 940px;
    font-weight: 300; font-size: 33px; line-height: 65px; text-align: center;
  }

  /* Footer */
  .footer {
    position: absolute; left: 0; top: 3439px; width: 1200px; height: 263px;
    background: var(--footer); color: var(--white); text-align: center;
  }
  .copyright {
    position: absolute; top: 164px; width: 100%;
    font-weight: 300; font-size: 36px; line-height: 56px;
  }
</style>
</head>
<body>
  <header class="hero" role="img" aria-label="Dark photograph of a farmhouse kitchen interior with a dining table and chairs">
    <div class="brand">BRAMBLEWOOD PRESS RELEASE</div>
    <h1 class="hero-title">A <span class="accent">BRAMBLEWOOD</span> AND A<br>CLEVER PELICAN</h1>
    <p class="hero-credit">WITH PHOTOGRAPHY - ROWAN HALE &amp; JASPER WREN</p>
  </header>

  <div class="intro-card"></div>
  <section class="intro">
    <p>An Interior Designer’s beautiful family account of a semi-rural lifestyle on the outskirts of the city of Sydney, Australia. A pictorial tale of the lifestyle and interiors of a family farmhouse, and their community, on Sydneys Northern Beaches.</p>
    <p>Included are poignant historical snippets of the area including a community profile on Australian of the Year, Martin Ellery, and insider information about where Pippin the Pelican once called home. An inspiring way to to live and love.</p>
  </section>

  <section class="book-frame">
    <div class="book-cover">
      <div class="cover-back" role="img" aria-label="Back cover with a faint black and white photograph of a horse">
        <p>An Interior Designer’s beautiful family account of a semi-rural lifestyle on the outskirts of the city of Sydney, Australia.</p>
        <p>A pictorial tale of the lifestyle and interiors of a family farmhouse, and their community, on Sydneys Northern Beaches.</p>
        <p>Included are poignant historical snippets of the area including a community profile on Australian of the Year, Martin Ellery, and insider information about where Pippin the Pelican once called home. An inspiring way to to live and love.</p>
      </div>
      <div class="cover-spine">
        <span class="spine-text">A BRAMBLEWOOD AND A CLEVER PELICAN<span class="spine-gap"></span>TESSA HALE</span>
      </div>
      <div class="cover-front">
        <div class="cover-photo" role="img" aria-label="Photograph of a dark panelled hallway leading to a bright window and desk"></div>
        <div class="cover-title">A <span class="accent">BRAMBLEWOOD</span> AND<br>A CLEVER PELICAN</div>
        <div class="cover-credit">WITH PHOTOGRAPHY - ROWAN HALE &amp; JASPER WREN</div>
        <div class="cover-author">TESSA HALE</div>
      </div>
    </div>
  </section>

  <div class="portrait-ring">
    <div class="portrait" role="img" aria-label="Portrait photograph of the author"></div>
  </div>
  <h2 class="about-title">ABOUT <span class="accent">TESSA HALE</span></h2>
  <p class="about-text">Lorem ipsum dolor sit amet, consectetur adipiscing elit, sed do eiusmod tempor incididunt ut labore et dolore magna aliqua. Quis ipsum suspendisse ultrices gravida. Risus commodo viverra maecenas accumsan lacus vel facilisiorem ipsum dolor sit amet, consectetur adipiscing elit, sed do eiusmod tempor incididunt ut labore et dolore magna aliquaipsum suspendisse ultrices gravidisus commodo viverra maecenas accumsan lacus vel facilisis.</p>

  <footer class="footer">
    <p class="copyright">© 2021&nbsp; Bramblewood. All rights reserved.Privacy Terms of Use</p>
  </footer>
</body>
</html>
```